Healthcare and Professional IT Services Company need a redesigned business card

We are a IT Services company that targets small medical practices and professional business such as Attorneys, Accounts, Architects etc. We want to communicate a professional yet friendly image using recent logo redesign here on Sketchforge. Like to see the colors blue and orange in the design. Must use the Copper Lantern Technology as displayed in the new logo - then also want to incorporate the fish logo as well.

Target Market(s)

Small medical and professional services

Industry/Entity Type

It Company

Contact Information for Business Card

The usual stuff, place for name address phone website. Also maybe our tagline which is "lit up by technology"

Requirements
Must have
• My new logo and the fish somewhere on the card

```html
<!DOCTYPE html>
<html lang="en">
<head>
<meta charset="utf-8">
<title>Copper Lantern Technology – Business Card</title>
<link href="https://fonts.googleapis.com/css2?family=Open+Sans:wght@400;600;700&display=swap" rel="stylesheet">
<style>
  :root {
    --backdrop: #2b2724;
    --card: #1a1a1a;
    --brand-blue: #27a4e0;
    --brand-orange: #f08a3c;
    --text-light: #f2f2f2;
  }
  * { box-sizing: border-box; margin: 0; padding: 0; }
  html, body {
    width: 1200px; height: 844px; overflow: hidden;
    background: var(--backdrop);
    font-family: "Open Sans", Arial, sans-serif;
  }
  .sheet {
    position: relative; width: 1200px; height: 844px;
    display: flex; align-items: center; justify-content: center; gap: 60px;
  }
  .card {
    position: relative; width: 540px; height: 310px;
    background: linear-gradient(120deg, var(--card) 0%, #222 70%, #2a2a2a 100%);
    box-shadow: 0 12px 30px rgba(0,0,0,.55);
    overflow: hidden;
  }

  /* Front */
  .band { position: absolute; left: 0; right: 0; height: 12px; background: var(--brand-blue); }
  .band--top { top: 0; }
  .band--bottom { bottom: 0; }
  .mascot-art {
    position: absolute; left: 22px; top: 100px; width: 170px; height: 150px;
    border-radius: 45% 50% 45% 40%;
    background: radial-gradient(circle at 60% 40%, #3fb6e6 0%, #2a8cc8 55%, var(--brand-orange) 100%);
  }
  .identity { position: absolute; left: 220px; top: 60px; }
  .identity__name {
    color: var(--brand-blue); font-weight: 700; font-size: 17px; letter-spacing: .5px;
    padding-bottom: 3px; border-bottom: 1px solid var(--brand-blue);
  }
  .identity__role { color: var(--text-light); font-size: 13px; margin-top: 3px; }
  .contact {
    position: absolute; left: 196px; right: 14px; top: 150px;
    list-style: none; text-align: center; color: var(--text-light);
    font-size: 14px; line-height: 21px; white-space: nowrap;
  }
  .contact__address { margin-top: 8px; font-size: 13.5px; }

  /* Back */
  .tab { position: absolute; width: 12px; height: 34px; background: var(--brand-blue); }
  .tab--left { left: 0; top: 190px; }
  .tab--right { right: 0; top: 60px; }
  .brand {
    position: absolute; left: 0; right: 0; top: 110px;
    display: flex; align-items: center; justify-content: center; gap: 10px;
  }
  .brand__mark { width: 14px; height: 14px; background: var(--brand-blue); }
  .brand__name { color: var(--brand-blue); font-weight: 700; font-size: 24px; white-space: nowrap; }
  .tagline {
    position: absolute; left: 0; right: 0; top: 195px; text-align: center;
    color: var(--brand-blue); font-weight: 700; font-size: 15px;
  }
</style>
</head>
<body>
<main class="sheet">
  <section class="card card--front" aria-label="Business card front">
    <div class="band band--top"></div>
    <div class="mascot-art" role="img" aria-label="Cartoon fish mascot illustration in blue and orange"></div>
    <div class="identity">
      <h1 class="identity__name">MORGAN HALE</h1>
      <p class="identity__role">Managing Director</p>
    </div>
    <ul class="contact">
      <li>123-456-7890</li>
      <li>infoname@yourwebsite.com</li>
      <li>www.website.com</li>
      <li class="contact__address">1234 Address Tag Line | Country Name, AB | 123456</li>
    </ul>
    <div class="band band--bottom"></div>
  </section>

  <section class="card card--back" aria-label="Business card back">
    <div class="tab tab--right"></div>
    <div class="brand">
      <span class="brand__mark"></span>
      <span class="brand__name">Copper Lantern Technology</span>
    </div>
    <p class="tagline">"lit up by technology"</p>
    <div class="tab tab--left"></div>
  </section>
</main>
</body>
</html>
```